PLM - Business Card Design Project

We need a business card based on our logo
Updates

Hi I just upload logo file in AI format Thanks and regards

Target Market(s)

Bank, Big companies, Business owners

Industry/Entity Type

Business

Font styles to use
Sans Serif

```html
<!DOCTYPE html>
<html lang="en">
<head>
<meta charset="utf-8">
<title>PLM Business Card</title>
<link rel="stylesheet" href="https://fonts.googleapis.com/css2?family=Mulish:wght@300;400;800&display=swap">
<style>
  :root {
    --page-bg: #e9ecef;
    --panel-light: #97dcf5;
    --blue-bright: #0a9be0;
    --blue-deep: #1068bb;
    --divider: #ffffff;
    --text-green: #0b6a3a;
    --brand-navy: #13284f;
  }
  html, body {
    margin: 0;
    padding: 0;
    width: 1200px;
    height: 799px;
    overflow: hidden;
    background: var(--page-bg);
  }
  .canvas {
    position: relative;
    width: 1200px;
    height: 799px;
  }
  .business-card {
    position: absolute;
    left: 110px;
    top: 124px;
    width: 980px;
    height: 551px;
    border-radius: 34px;
    overflow: hidden;
    background: radial-gradient(circle at 62% 48%, var(--blue-bright) 0%, var(--blue-deep) 75%);
    box-shadow: 0 14px 34px rgba(0, 0, 0, 0.22);
  }
  .card-shape {
    position: absolute;
    inset: 0;
    width: 100%;
    height: 100%;
  }
  .contact-block {
    position: absolute;
    left: 78px;
    top: 196px;
    max-width: 370px;
    color: var(--text-green);
    font-family: "Mulish", sans-serif;
  }
  .company-name {
    margin: 0 0 20px;
    font-size: 25px;
    font-weight: 800;
    letter-spacing: -0.2px;
    white-space: nowrap;
  }
  .address {
    margin: 0;
    padding-left: 8px;
    font-size: 22px;
    font-weight: 400;
    line-height: 1.12;
    font-style: normal;
    white-space: nowrap;
  }
  .brand-name {
    position: absolute;
    left: 560px;
    top: 190px;
    margin: 0;
    font-family: "Mulish", sans-serif;
    font-weight: 300;
    font-size: 160px;
    line-height: 1;
    letter-spacing: 2px;
    color: var(--brand-navy);
  }
</style>
</head>
<body>
<main class="canvas">
  <section class="business-card" aria-label="PLM business card">
    <svg class="card-shape" viewBox="0 0 980 551" preserveAspectRatio="none" aria-hidden="true">
      <path d="M0 0 H440 C530 110 520 420 240 551 H0 Z" fill="var(--panel-light)"/>
      <path d="M440 0 C530 110 520 420 240 551" fill="none" stroke="var(--divider)" stroke-width="4"/>
    </svg>
    <div class="contact-block">
      <h2 class="company-name">Cabinet Marlowe &amp; Associes</h2>
      <address class="address">
        1840 W Juniper Avenue Suite<br>
        4 Reno<br>
        Nevada 89502
      </address>
    </div>
    <h1 class="brand-name">PLM</h1>
  </section>
</main>
</body>
</html>
```